Cutting Board Oil Label

I would like a label created for our custom made cutting board oil. The bottle will be clear and come in several different sizes. I have included the current label we use. We would like the information to stay the same, but more aesthetically pleasing and professionally presented. I am also including our logo and the current label of our biggest competitor.

```html
<!DOCTYPE html>
<html lang="en">
<head>
<meta charset="utf-8">
<title>Cutting Board Conditioner Label</title>
<link href="https://fonts.googleapis.com/css2?family=Arvo:wght@700&family=Mulish:wght@400&display=swap" rel="stylesheet">
<style>
  :root {
    --teal: #22bfc9;
    --copper: #c57f3f;
    --slate: #76787b;
    --ink: #1d1d1f;
    --wood-light: #ecc9a3;
    --wood: #dc9f66;
    --wood-deep: #cf8c52;
    --tomato: #e5321f;
    --paper: #ffffff;
    --backdrop: #ffffff;
  }
  html, body {
    margin: 0;
    padding: 0;
    width: 1200px;
    height: 761px;
    overflow: hidden;
    background: var(--backdrop);
  }
  .label {
    position: absolute;
    left: 90px;
    top: 41px;
    width: 1019px;
    height: 679px;
    box-sizing: border-box;
    border: 10px solid var(--teal);
    background: var(--paper);
    font-family: "Mulish", sans-serif;
  }
  .side-copy {
    position: absolute;
    width: 616px;
    transform: rotate(-90deg);
    transform-origin: top left;
    font-size: 16.5px;
    line-height: 1.35;
    color: var(--ink);
    margin: 0;
    white-space: nowrap;
  }
  .side-copy.directions { left: 31px; top: 638px; }
  .side-copy.care { left: 864px; top: 638px; font-size: 15.5px; }
  .brand-name {
    position: absolute;
    left: 160px;
    top: 58px;
    width: 660px;
    text-align: center;
    font-family: "Arvo", serif;
    font-weight: 700;
    font-size: 50px;
    color: var(--slate);
    margin: 0;
  }
  .product-title {
    position: absolute;
    left: 160px;
    top: 148px;
    width: 660px;
    text-align: center;
    margin: 0;
    font-family: "Arvo", serif;
    font-weight: 700;
    color: var(--copper);
  }
  .product-title .line-small { display: block; font-size: 50px; line-height: 64px; letter-spacing: 2px; }
  .product-title .line-large { display: block; font-size: 74px; line-height: 84px; }
  .uses {
    position: absolute;
    left: 160px;
    top: 292px;
    width: 660px;
    text-align: center;
    margin: 0;
    font-family: "Arvo", serif;
    font-weight: 700;
    font-size: 21px;
    line-height: 32px;
    color: var(--slate);
  }
  .finish-panel {
    position: absolute;
    left: 164px;
    top: 366px;
    width: 679px;
    height: 230px;
    background: linear-gradient(180deg, var(--wood) 0%, var(--wood-deep) 100%);
  }
  .finish-panel .raw-wood {
    position: absolute;
    left: 0; top: 0;
    width: 152px; height: 100%;
    background: var(--wood-light);
  }
  .claim {
    position: absolute;
    left: 168px;
    top: 14px;
    margin: 0;
    font-family: "Arvo", serif;
    font-weight: 700;
    font-size: 40px;
    line-height: 54px;
    color: var(--paper);
    letter-spacing: 1px;
  }
  .tomato {
    position: absolute;
    left: 546px;
    top: 9px;
    width: 112px;
    height: 112px;
    border-radius: 50%;
    background: radial-gradient(circle at 40% 35%, #f26a4e 0%, var(--tomato) 55%, #b81e12 100%);
  }
  .ingredients {
    position: absolute;
    left: 260px;
    top: 130px;
    margin: 0;
    font-size: 21px;
    line-height: 28px;
    color: var(--paper);
  }
  .stage {
    position: absolute;
    bottom: 8px;
    font-family: "Arvo", serif;
    font-weight: 700;
    font-size: 18px;
    letter-spacing: 1.5px;
    color: var(--copper);
  }
  .stage.before { left: 63px; }
  .stage.after { left: 168px; color: var(--paper); }
  .footer {
    position: absolute;
    left: 200px;
    top: 608px;
    width: 600px;
    height: 50px;
    display: flex;
    align-items: center;
    font-family: "Arvo", serif;
    font-weight: 700;
    color: var(--slate);
  }
  .origin { font-size: 15px; }
  .flag {
    width: 88px;
    height: 44px;
    margin: 0 18px 0 10px;
    background: linear-gradient(180deg, #3a4e9c 0%, #3a4e9c 45%, #d6303a 45%, #f1f1f1 70%, #d6303a 100%);
  }
  .site { font-size: 16px; letter-spacing: 0.5px; }
</style>
</head>
<body>
  <div class="label">
    <p class="side-copy directions">Directions: Apply a generous amount of conditioner with a clean,<br>lint free cloth. For best results, allow board to soak<br>in conditioner overnight.<br>Using a clean, lint free cloth, buff and remove any excess conditioner.</p>

    <p class="brand-name">Laurel Hollow Goods</p>

    <h1 class="product-title">
      <span class="line-small">Cutting Board</span>
      <span class="line-large">CONDITIONER</span>
    </h1>

    <p class="uses">For use on cutting boards, butcher blocks,<br>wood utensils, and any other wood products.</p>

    <div class="finish-panel" role="img" aria-label="Wood grain showing an untreated board beside a conditioned board">
      <div class="raw-wood"></div>
      <p class="claim">FOOD SAFE -<br>ALL NATURAL</p>
      <div class="tomato" role="img" aria-label="Photo of a ripe red tomato"></div>
      <p class="ingredients">Made with:<br>Beeswax, Mineral Oil, Orange Oil,<br>Lemon Oil, and Vitamin E</p>
      <span class="stage before">before</span>
      <span class="stage after">after</span>
    </div>

    <div class="footer">
      <span class="origin">Made in the USA</span>
      <div class="flag" role="img" aria-label="Waving American flag"></div>
      <span class="site">www.LaurelHollowGoods.com</span>
    </div>

    <p class="side-copy care">For new or unconditioned cutting boards,<br>butcher blocks, or wooden kitchen utensils we recommend repeating<br>the process a second time to ensure your wood is properly sealed.<br>Recondition about once a month (depending on frequency<br>of use) or when the board begins to become dry to the touch.</p>
  </div>
</body>
</html>
```